Business Card - Apex Wellness

Please use the logo / design elements and font to design a business card that is eye catching and informative. If using "Direct Primary Care" logo element, you don't have to spell it out in the text.

Dr. Brendan Halvik
Apex Wellness - Direct Primary Care
4817 Tillbrook Rd. Suite 305
Lindenport, CO 80999
Phone: 720-555-0137
ApexWellnessAR.example

```html
<!DOCTYPE html>
<html lang="en">
<head>
<meta charset="utf-8">
<title>Apex Wellness – Business Card</title>
<link rel="stylesheet" href="https://fonts.googleapis.com/css2?family=Montserrat:wght@600&family=Questrial&display=swap">
<style>
  :root {
    --page-bg: #e4e3e6;
    --navy: #030828;
    --navy-soft: #0d1838;
    --paper: #efefef;
    --ink: #0a0f2c;
    --cyan: #2ba6df;
    --blue: #2a63c9;
    --white: #f4f5f8;
    --rule: #1f7fc4;
  }
  * { box-sizing: border-box; margin: 0; padding: 0; }
  html, body { width: 1200px; height: 900px; overflow: hidden; }
  body {
    background: var(--page-bg);
    font-family: "Questrial", "Century Gothic", sans-serif;
    display: flex;
    align-items: center;
    justify-content: center;
    gap: 50px;
  }
  .card {
    position: relative;
    width: 525px;
    height: 300px;
    border-radius: 3px;
    overflow: hidden;
    box-shadow: 0 18px 40px rgba(0,0,0,.25);
  }
  .card--front { background: var(--navy); color: var(--white); }
  .card--back { background: var(--paper); display: flex; align-items: center; justify-content: center; }

  .front__circle {
    position: absolute;
    width: 130px; height: 130px;
    right: 70px; top: 95px;
    border-radius: 50%;
    background: var(--navy-soft);
  }

  .wordmark {
    display: flex;
    align-items: center;
    gap: 10px;
    font-family: "Montserrat", sans-serif;
    font-weight: 600;
    letter-spacing: .5px;
  }
  .wordmark__dot { border-radius: 50%; flex: none; }

  .front__brand {
    position: absolute;
    top: 34px; right: 34px;
    font-size: 30px;
    color: var(--white);
  }
  .front__brand .wordmark__dot { width: 16px; height: 16px; background: var(--cyan); }

  .person {
    position: absolute;
    left: 34px; top: 120px;
  }
  .person__name {
    font-family: "Montserrat", sans-serif;
    font-weight: 600;
    font-size: 19px;
    color: var(--cyan);
  }
  .person__role { font-size: 15px; margin-top: 4px; }

  .contact {
    position: absolute;
    left: 34px; right: 34px; bottom: 26px;
    font-size: 13.5px;
  }
  .contact__row { display: flex; align-items: center; gap: 8px; margin-bottom: 5px; }
  .contact__icon { width: 13px; height: 13px; flex: none; }
  .contact__rule { height: 1px; background: var(--rule); margin: 10px 0 8px; width: 82%; }
  .contact__practice {
    font-family: "Montserrat", sans-serif;
    font-weight: 600;
    font-size: 13px;
    color: var(--blue);
  }
  .contact__address { margin-top: 3px; }

  .back__brand { font-size: 38px; color: var(--ink); }
  .back__brand .wordmark__dot { width: 20px; height: 20px; background: var(--blue); }
</style>
</head>
<body>

  <article class="card card--front" aria-label="Business card front">
    <div class="front__circle"></div>

    <div class="wordmark front__brand">
      <span class="wordmark__dot"></span>
      <span>Apex Wellness</span>
    </div>

    <div class="person">
      <p class="person__name">Dr. Brendan Halvik</p>
      <p class="person__role">Specialty of Family Medicine</p>
    </div>

    <div class="contact">
      <p class="contact__row">
        <svg class="contact__icon" viewBox="0 0 24 24" aria-hidden="true"><path fill="#2a63c9" d="M6.6 10.8a15.1 15.1 0 0 0 6.6 6.6l2.2-2.2a1 1 0 0 1 1-.25 11.4 11.4 0 0 0 3.6.57 1 1 0 0 1 1 1V20a1 1 0 0 1-1 1A17 17 0 0 1 3 4a1 1 0 0 1 1-1h3.5a1 1 0 0 1 1 1c0 1.25.2 2.45.57 3.57a1 1 0 0 1-.25 1z"/></svg>
        <span>720-555-0137</span>
      </p>
      <p class="contact__row">
        <svg class="contact__icon" viewBox="0 0 24 24" aria-hidden="true" fill="none" stroke="#2a63c9" stroke-width="1.8"><circle cx="12" cy="12" r="9"/><ellipse cx="12" cy="12" rx="4" ry="9"/><path d="M3 12h18M5 7h14M5 17h14"/></svg>
        <span>ApexWellnessAR.example</span>
      </p>
      <div class="contact__rule"></div>
      <p class="contact__practice">Apex Wellness - Direct Primary Care</p>
      <p class="contact__address">4817 Tillbrook Rd. Suite 305, Lindenport, CO 80999</p>
    </div>
  </article>

  <article class="card card--back" aria-label="Business card back">
    <div class="wordmark back__brand">
      <span class="wordmark__dot"></span>
      <span>Apex Wellness</span>
    </div>
  </article>

</body>
</html>
```